Menu: A4 (double sided) Lunch/Dinner Menu (one side) + Pizza Menu (other side)

Hello.
We would like to create a new style of menus.
Must be easy to read - a summer feel, crisp, clean, beachy, possible retro feel, colours probably based on our website colours (see address below).
Simple and casual is best as we are a casual beachside Cafe.
This menu will be double sided therefore this job is 2 pages.
If you win this job we will have 2 or 3 more menus for you to create soon after (Drinks, Breakfast, possibly a small Kids menu).
The paper for these menus we expect will be a nice white paper which will then be matte laminated.
Colours possible are the green colour #3a6066, the terracotta on our website logo border and website buttons, maybe a little yellow but must be easy to read on white paper.
Black for text might be okay if this is your best design option.
Please view our website and take a feel for the business, location, the existing website branding and website colours we are trying to achieve, www.saltwrencafe.com.au
We prefer to avoid overwhelming the guest with too many colours on the menus (hence the white paper) as the building is so colourful (La Boca, Argentina, inspired) and the guest experience can be complimented via crisp easy to read menus.
IMPORTANT:
The menus provided please must be fully and easily editable by us in the future.
If you win the job, you must please provide clear instructions on how our staff can edit the menus in the future if project is delivered in Adobe format. Word is also an option for us if you like.
As such, we have attached some documents: the 2x Word documents for the text, 2x .pdf so you can see the fonts and style we were using previously (was printing on recycled brown paper then matte laminated).
If you wished to use the SeaLife Font (this is the existing Font for headings) please let us know as we purchased that font and can provide it.
We have also attached a menu from Quillmont Hotel which we feel has a nice retro feel.
Please include our Instagram in 1 place on the menu @saltwrencafe
Finally, please note,
we never wish to waste anyone's time so we will narrow down the submissions quickly based on first drafts (please know this is because we appreciate your effort and know your time is valuable) and we will then work with the top designer to finalise in a professional fashion.
Thank you.

```html
<!DOCTYPE html>
<html lang="en">
<head>
<meta charset="utf-8">
<title>Salt Wren Cafe — Lunch + Dinner and Pizza Menus</title>
<link href="https://fonts.googleapis.com/css2?family=Alfa+Slab+One&family=Bungee&family=Montserrat:ital,wght@0,400;0,500;0,700;1,500;1,700&display=swap" rel="stylesheet">
<style>
:root{
  --yellow:#fff200;
  --teal:#2f4d57;
  --navy:#17357a;
  --terracotta:#b4461a;
  --ink:#2b2b2b;
  --muted:#555;
  --rule:#9a9a9a;
  --board:#e6e8eb;
  --paper:#ffffff;
  --paper-fade:#eef1f4;
  --sketch:#e3e6ea;
}
*{box-sizing:border-box;margin:0;padding:0}
html,body{width:1200px;height:3857px;overflow:hidden}
body{background:var(--board);font-family:"Montserrat",sans-serif;color:var(--ink);position:relative}
.menu-page{position:absolute;left:70px;width:1060px;height:1500px;background:linear-gradient(180deg,var(--paper) 55%,var(--paper-fade) 100%);box-shadow:0 6px 18px rgba(0,0,0,.18);overflow:hidden}
.page-lunch{top:280px}
.page-pizza{top:2060px}
.page-header{position:absolute;left:0;top:0;width:1060px;height:200px}
.band-yellow{position:absolute;left:0;top:0;width:1060px;height:60px;background:var(--yellow)}
.band-teal{position:absolute;left:0;top:60px;width:1060px;height:100px;background:var(--teal)}
.header-art{position:absolute;top:78px;height:64px;border-radius:8px;background:linear-gradient(90deg,#c9703d,#e2b04a,#8fb7c0)}
.header-art.left{left:22px;width:250px}
.header-art.right{right:22px;width:250px}
.pizza .header-art{background:linear-gradient(90deg,#d8642c,#f0b34a,#d8642c)}
.brand{position:absolute;left:300px;top:60px;width:460px;height:100px;display:flex;align-items:center;justify-content:center;font-family:"Montserrat",sans-serif;font-weight:700;color:var(--paper);font-size:34px;letter-spacing:3px;white-space:nowrap}
.title-row{position:absolute;left:0;top:220px;width:1060px;height:80px}
.title-bar{position:absolute;top:14px;width:130px;height:48px}
.title-bar.left{left:0;background:linear-gradient(180deg,var(--terracotta) 50%,var(--yellow) 50%)}
.title-bar.right{right:0;background:linear-gradient(180deg,var(--yellow) 50%,var(--terracotta) 50%)}
.page-title{position:absolute;left:0;right:0;top:0;text-align:center;font-family:"Alfa Slab One",serif;font-size:70px;line-height:78px;color:var(--navy);letter-spacing:1px}
.section-label{position:absolute;left:50%;transform:translateX(-50%);background:var(--yellow);border:2px solid var(--terracotta);font-family:"Bungee",sans-serif;color:var(--navy);font-size:26px;line-height:38px;padding:0 14px;white-space:nowrap}
.columns{position:absolute;left:45px;width:970px;display:grid;grid-template-columns:1fr 1fr;column-gap:70px}
.col-head{text-align:right;color:var(--terracotta);font-weight:700;font-size:15px;height:18px}
.item{margin-top:16px}
.item-row{display:grid;grid-template-columns:auto 1fr auto;align-items:baseline;column-gap:8px}
.item-name{font-weight:700;font-size:15px;color:var(--ink)}
.item-name.caps{text-transform:uppercase}
.leader{border-bottom:1.5px dashed var(--rule);transform:translateY(-4px)}
.price{font-weight:700;font-size:15px;color:var(--ink);min-width:22px;text-align:right}
.item-desc{font-size:13px;line-height:17px;color:var(--muted);margin-top:2px;max-width:400px}
.veg{color:var(--terracotta);font-weight:700;font-style:normal;font-size:13px}
.gfo{color:var(--navy);font-weight:700;font-style:italic;font-size:12px}
.extra{font-size:13px;font-weight:500;font-style:italic;color:var(--navy);margin-top:2px}
.sketch{position:absolute;background:var(--sketch);border-radius:40px;opacity:.75}
.page-footer{position:absolute;left:40px;right:40px;bottom:40px;height:40px;display:flex;align-items:center;gap:26px;font-size:12px;font-weight:700;color:var(--navy)}
.arrows{color:var(--terracotta);font-size:22px;letter-spacing:14px}
.legend{display:flex;align-items:center;gap:8px}
.legend b{font-size:26px;color:var(--terracotta);font-family:"Montserrat",sans-serif}
.legend span{border-bottom:1.5px solid var(--navy);padding-bottom:2px}
.spacer{flex:1}
.subtitle{position:absolute;left:0;right:0;top:302px;text-align:center;font-weight:700;font-size:15px;letter-spacing:1px;color:var(--ink)}
.sides{position:absolute;left:45px;width:970px;top:345px;display:flex;justify-content:space-between}
.side-pill{border:2px solid var(--ink);border-radius:16px;padding:3px 24px;font-weight:700;font-size:14px;color:var(--terracotta)}
.allergy{position:absolute;left:45px;top:1310px;width:440px;font-size:12px;line-height:15px;color:var(--muted)}
.allergy h3{color:var(--terracotta);font-size:13px;margin-bottom:4px}
.badge-strip{position:absolute;left:562px;top:1312px;width:450px;height:82px;background:var(--yellow);border-radius:4px;display:flex;justify-content:space-around;align-items:center}
.badge{width:66px;height:66px;border-radius:50%;background:#f5c400;border:3px solid var(--terracotta)}
</style>
</head>
<body>

<section class="menu-page lunch page-lunch">
  <header class="page-header">
    <div class="band-yellow"></div>
    <div class="band-teal"></div>
    <div class="header-art left" role="img" aria-label="Illustrated lunchbox, drink carton and burger icons"></div>
    <div class="header-art right" role="img" aria-label="Illustrated sandwich, bento box and sushi icons"></div>
    <div class="brand">SALT WREN CAFE</div>
  </header>

  <div class="title-row">
    <div class="title-bar left"></div>
    <h1 class="page-title">LUNCH + DINNER</h1>
    <div class="title-bar right"></div>
  </div>

  <div class="sketch" style="left:150px;top:330px;width:240px;height:60px" role="img" aria-label="Line sketch of vegetables"></div>
  <div class="sketch" style="left:700px;top:320px;width:160px;height:80px" role="img" aria-label="Line sketch of pea pod and tomato"></div>
  <h2 class="section-label" style="top:320px">ENTREE</h2>

  <div class="columns" style="top:395px">
    <div>
      <div class="col-head">(s)</div>
      <div class="item"><div class="item-row"><span class="item-name">Garlic Bread (2) <i class="veg">v</i></span><span class="leader"></span><span class="price">8</span></div></div>
      <div class="item"><div class="item-row"><span class="item-name">Salt &amp; Pepper Squid</span><span class="leader"></span><span class="price">18</span></div><p class="item-desc">w/ thai dipping sauce</p></div>
      <div class="item"><div class="item-row"><span class="item-name">Duo of Dip <i class="veg">v</i></span><span class="leader"></span><span class="price">14</span></div><p class="item-desc">w/ pita</p></div>
      <div class="item"><div class="item-row"><span class="item-name">Bowl of Chips <i class="veg">v</i></span><span class="leader"></span><span class="price">11</span></div><p class="item-desc">w/ tomato sauce</p></div>
    </div>
    <div>
      <div class="col-head">(s)</div>
      <div class="item"><div class="item-row"><span class="item-name">Seasoned Wedges <i class="veg">v</i></span><span class="leader"></span><span class="price">15</span></div><p class="item-desc">w/ sour cream &amp; sweet chilli</p></div>
      <div class="item"><div class="item-row"><span class="item-name">Onion Rings (12) <i class="veg">v</i></span><span class="leader"></span><span class="price">13</span></div><p class="item-desc">beer battered w/ tangy mayo</p></div>
      <div class="item"><div class="item-row"><span class="item-name">Vietnamese Spring Rolls (3)</span><span class="leader"></span><span class="price">11</span></div><p class="item-desc">Chicken, home-made</p></div>
      <div class="item"><div class="item-row"><span class="item-name">Bruschetta (1) <i class="veg">v</i></span><span class="leader"></span><span class="price">10</span></div><p class="item-desc">w/ olive oil, tomato &amp; red onion salsa, balsamic glaze, feta</p></div>
    </div>
  </div>

  <div class="sketch" style="left:150px;top:660px;width:300px;height:70px" role="img" aria-label="Line sketch of fish, salmon steak and squid"></div>
  <div class="sketch" style="left:640px;top:650px;width:260px;height:70px" role="img" aria-label="Line sketch of crab and prawns"></div>
  <h2 class="section-label" style="top:670px">MAINS</h2>

  <div class="columns" style="top:745px">
    <div>
      <div class="col-head">(s)</div>
      <div class="item"><div class="item-row"><span class="item-name caps">The Fish &amp; Chips</span><span class="leader"></span><span class="price">25</span></div><p class="item-desc">House-crumbed butterfish w/ chips, tartare &amp; side salad</p></div>
      <div class="item"><div class="item-row"><span class="item-name">Smokey beef &amp; bacon cheese burger</span><span class="leader"></span><span class="price">23</span></div><p class="item-desc">w/ chips, onion rings, gerkins &amp; tangy mayo</p><p class="extra">+Jalapenos 2 &nbsp;&nbsp; + Pineapple 2</p></div>
      <div class="item"><div class="item-row"><span class="item-name caps">Salt &amp; Pepper Squid</span><span class="leader"></span><span class="price">31</span></div><p class="item-desc">Golden tangles w/ chips, thai dipping sauce &amp; side salad</p></div>
    </div>
    <div>
      <div class="col-head">(s)</div>
      <div class="item"><div class="item-row"><span class="item-name caps">Seafood Basket</span><span class="leader"></span><span class="price">31</span></div><p class="item-desc">Crumbed butterfish, grilled prawns, salt &amp; pepper squid, chips, tartare &amp; side salad</p></div>
      <div class="item"><div class="item-row"><span class="item-name caps">Atlantic Salmon</span><span class="leader"></span><span class="price">31</span></div><p class="item-desc">Served w/ mash, teriyaki sauce &amp; winter vegetables</p></div>
      <div class="item"><div class="item-row"><span class="item-name caps">Chicken Parmigiana</span><span class="leader"></span><span class="price">13</span></div><p class="item-desc">House-crumbed breast schnitzel, napoli sauce, mozzarella, chips &amp; side salad</p><p class="extra">+ bacon and pineapple 4 &nbsp;&nbsp; + jalapenos and pineapple 4</p></div>
    </div>
  </div>

  <div class="sketch" style="left:20px;top:1010px;width:160px;height:70px" role="img" aria-label="Line sketch of cured meats"></div>
  <div class="sketch" style="left:880px;top:1010px;width:160px;height:70px" role="img" aria-label="Line sketch of salami and sausage"></div>
  <h2 class="section-label" style="top:1025px">SALT WREN PLATTER FOR 2</h2>

  <div class="columns" style="top:1085px">
    <div>
      <div class="col-head">(s)</div>
      <div class="item"><div class="item-row"><span class="item-name caps">Beer battered flathead, salt &amp;</span><span class="leader"></span><span class="price">90</span></div><p class="item-desc" style="font-weight:700;color:var(--ink);font-size:14px;text-transform:uppercase">pepper squid, prawn skewers, grilled chicken, lamb &amp; chorizo, served with antipasto, dipping sauces, pita &amp; garlic bread</p><p class="extra" style="font-size:14px">(+45 pp)</p></div>
      <div class="item"><div class="item-row"><span class="item-name caps">New York Sirloin <i class="gfo">gfo</i></span><span class="leader"></span><span class="price">38</span></div><p class="item-desc"><b>400g MSA w/ mash &amp; winter vegetables</b><br>Choose: mushroom gravy or classic gravy</p><p class="extra">or surf ‘n’ turf gfo +6</p></div>
      <div class="item"><div class="item-row"><span class="item-name caps">Chicken Caesar</span><span class="leader"></span><span class="price">27</span></div><p class="item-desc">w/ bacon, anchovies, egg, caesar dressing, parmesan, spanish onion, garlic bread</p></div>
    </div>
    <div>
      <div class="col-head">(s)</div>
      <div class="item"><div class="item-row"><span class="item-name caps">Lamb Salad <i class="gfo">gfo</i></span><span class="leader"></span><span class="price">30</span></div><p class="item-desc">skewers w/ traditional greek salad, tzatziki &amp; garlic bread<br>+ extra lamb &nbsp;8</p></div>
      <div class="item"><div class="item-row"><span class="item-name caps">Thai Chicken Curry <i class="gfo">gfo</i></span><span class="leader"></span><span class="price">26</span></div><p class="item-desc"><b>Mild</b> traditional recipe, w/ jasmine rice &amp; papadums</p></div>
      <div class="item"><div class="item-row"><span class="item-name caps">Beach Burger</span><span class="leader"></span><span class="price">23</span></div><p class="item-desc"><i class="veg">v</i> traditional recipe, w/ jasmine rice &amp; papadums</p></div>
      <div class="item"><div class="item-row"><span class="item-name caps">Vegan Curry <span style="font-weight:500;text-transform:none;font-size:13px">Mild</span> <i class="gfo">gfo</i><i class="veg">v</i></span><span class="leader"></span><span class="price">24</span></div><p class="item-desc">Chickpea &amp; pumpkin w/ fresh tomatoes &amp; basil, jasmine rice &amp; papadums</p></div>
    </div>
  </div>

  <footer class="page-footer">
    <span class="arrows">→→→</span>
    <span class="legend" style="margin-left:60px"><b>V</b><span>VEGETARIAN</span></span>
    <span class="legend"><b>GFO</b><span>GLUTEN FRIENDLY OPTIONAL, PLEASE ASK</span></span>
    <span class="spacer"></span>
    <span class="arrows">←←←</span>
  </footer>
</section>

<section class="menu-page pizza page-pizza">
  <header class="page-header">
    <div class="band-yellow"></div>
    <div class="band-teal"></div>
    <div class="header-art left" role="img" aria-label="Three illustrated pizzas"></div>
    <div class="header-art right" role="img" aria-label="Three illustrated pizzas"></div>
    <div class="brand">SALT WREN CAFE</div>
  </header>

  <div class="title-row">
    <div class="title-bar left"></div>
    <h1 class="page-title">PIZZA</h1>
    <div class="title-bar right"></div>
  </div>
  <p class="subtitle">ALL 12” WITH HOUSE-MADE TOMATO BASE &amp; MOZZARELLA</p>

  <div class="sides">
    <span class="side-pill">Garlic Bread &nbsp;$8</span>
    <span class="side-pill">Greek Salad &nbsp;$16</span>
    <span class="side-pill">Garden Salad &nbsp;$12</span>
  </div>

  <div class="sketch" style="left:0;top:400px;width:330px;height:70px" role="img" aria-label="Line sketch of pizza toppings"></div>
  <div class="sketch" style="left:770px;top:400px;width:250px;height:70px" role="img" aria-label="Line sketch of mushroom, tomato and chilli"></div>
  <h2 class="section-label" style="top:415px">STANDARD</h2>

  <div class="columns" style="top:475px">
    <div>
      <div class="col-head">(s)</div>
      <div class="item"><div class="item-row"><span class="item-name caps">Hawaiian</span><span class="leader"></span><span class="price">22</span></div><p class="item-desc">Ham, Pineapple</p></div>
      <div class="item"><div class="item-row"><span class="item-name caps">Margherita <i class="veg">v</i></span><span class="leader"></span><span class="price">22</span></div><p class="item-desc">Marinated &amp; diced tomatoes, fresh basil</p></div>
      <div class="item"><div class="item-row"><span class="item-name caps">BBQ Chicken</span><span class="leader"></span><span class="price">**</span></div><p class="item-desc">Chicken, salami, tomato, spanish onion, bbq sauce</p></div>
      <div class="item"><div class="item-row"><span class="item-name caps">Chorizo</span><span class="leader"></span><span class="price">**</span></div><p class="item-desc">Chorizo, salami, tomato, mushrooms, spanish onion</p></div>
      <div class="item"><div class="item-row"><span class="item-name caps">Salt Wren Special</span><span class="leader"></span><span class="price">**</span></div><p class="item-desc">Ham, salami, prawns, kalamata olives, roasted capsicum, mushrooms, spanish onion</p></div>
      <div class="item"><div class="item-row"><span class="item-name caps">Meat Lovers</span><span class="leader"></span><span class="price">**</span></div><p class="item-desc">Chicken, bacon, salami, ham, bbq sauce</p></div>
    </div>
    <div>
      <div class="col-head">(s)</div>
      <div class="item"><div class="item-row"><span class="item-name caps">Mona Lisa</span><span class="leader" style="border:0"></span><span class="price"></span></div><p class="item-desc">Chicken, pineapple, ham, spanish onion, mushrooms</p></div>
      <div class="item"><div class="item-row"><span class="item-name caps">Puttanesca</span><span class="leader"></span><span class="price">**</span></div><p class="item-desc">Anchovies, capers, salami, kalamata olives, roasted capsicum, parmesan</p></div>
      <div class="item"><div class="item-row"><span class="item-name caps">Tropical Chicken</span><span class="leader"></span><span class="price">**</span></div><p class="item-desc">Chicken, pineapple, spanish onion, chilli, tomato, mushrooms</p></div>
      <div class="item"><div class="item-row"><span class="item-name caps">Vegetarian <i class="veg">v</i></span><span class="leader"></span><span class="price">**</span></div><p class="item-desc">Roasted capsicum, tomato, mushrooms, artichokes, kalamata olives, spanish onion</p></div>
      <div class="item"><div class="item-row"><span class="item-name caps">Build Your Own <i class="veg">v</i></span><span class="leader"></span><span class="price">All 26</span></div><p class="item-desc">Tomato base, mozzarella &amp; four toppings</p></div>
    </div>
  </div>

  <div class="sketch" style="left:0;top:935px;width:330px;height:80px" role="img" aria-label="Line sketch of lemon and pumpkin"></div>
  <div class="sketch" style="left:690px;top:935px;width:370px;height:80px" role="img" aria-label="Line sketch of pumpkin, chicken and salami"></div>
  <h2 class="section-label" style="top:955px">GOURMET</h2>

  <div class="columns" style="top:1010px">
    <div>
      <div class="col-head">(s)</div>
      <div class="item"><div class="item-row"><span class="item-name caps">Caveman</span><span class="leader" style="border:0"></span><span class="price"></span></div><p class="item-desc">Chicken, lamb, pork sausage, chorizo, salami, bacon, spanish onion, caramelised onion, smokey bbq sauce</p></div>
      <div class="item"><div class="item-row"><span class="item-name caps">Spicy Prawn &amp; Basil Pesto</span><span class="leader" style="border:0"></span><span class="price"></span></div><p class="item-desc">Prawns, roasted capsicum, chilli, spring onion, basil</p></div>
      <div class="item"><div class="item-row"><span class="item-name caps">Gourmet Vegetarian <i class="veg">v</i></span><span class="leader" style="border:0"></span><span class="price"></span></div><p class="item-desc">Pumpkin, eggplant, semi-dried tomatoes, roasted capsicum, red onion, bulgarian feta, kalamata olives, spinach</p></div>
    </div>
    <div>
      <div class="col-head">(s)</div>
      <div class="item"><div class="item-row"><span class="item-name caps">Rusty Spur</span><span class="leader" style="border:0"></span><span class="price"></span></div><p class="item-desc">Chilli jam, jalapeno peppers, mushrooms, bacon, chilli, chorizo, spanish onion</p></div>
      <div class="item"><div class="item-row"><span class="item-name caps">Lamb Pizza</span><span class="leader" style="border:0"></span><span class="price"></span></div><p class="item-desc">Lamb, red onion, fresh tomato, tzatziki, spring onion</p></div>
      <div class="item"><div class="item-row"><span class="item-name caps">Los Pollos</span><span class="leader" style="border:0"></span><span class="price"></span></div><p class="item-desc">Chicken, pumpkin, basil pesto, spinach, feta, pine nuts</p></div>
      <div class="item"><div class="item-row"><span class="item-name caps">Seafood Pizza</span><span class="leader"></span><span class="price">All 29</span></div><p class="item-desc">Array of seafood</p></div>
    </div>
  </div>

  <div class="allergy">
    <h3>Allergies? Please let us know!</h3>
    <p>All care is taken to cater for allergies including gluten, however our kitchen is small and we do not have separate preparation or cooking areas. As such, there is risk of cross-contact with your allergen and we are unable to guarantee allergen-free meals. Olives may very rarely contain pips.</p>
  </div>
  <div class="badge-strip">
    <span class="badge"></span><span class="badge"></span><span class="badge"></span><span class="badge"></span>
  </div>

  <footer class="page-footer">
    <span class="arrows">→→→</span>
    <span class="legend" style="margin-left:60px"><b>V</b><span>VEGETARIAN</span></span>
    <span class="legend"><b>+$4</b><span>GLUTEN FREE BASE</span></span>
    <span class="legend"><b>+$3</b><span>VEGAN CHEESE</span></span>
    <span class="spacer"></span>
    <span class="arrows">←←←</span>
  </footer>
</section>

</body>
</html>
```